bluefernworks.com website design

We're looking for a website design for Bluefernworks.com .
Bluefern is a manufacturer of high visibility traffic safety equipment and gear.. Our initial site will be a product catalog site featuring traffic cones . We will eventually expand to include traffic barriers, mesh signs, safety clothing and more. Our logo and product pictures can be found at bluefernworks.com .
Updates

Target Market(s)

We service a wide range of customers with our focus markets being construction, manufacturing and municipalities.

Industry/Entity Type

Safety Products

Number of Pages Required

1 page

Font styles to use
Sans Serif

Requirements
Must have
• company logo w/compatible color scheme

```html
<!DOCTYPE html>
<html lang="en">
<head>
<meta charset="utf-8">
<title>Bluefern Safety Products</title>
<link rel="stylesheet" href="https://fonts.googleapis.com/css2?family=Poppins:wght@300;400;500;600&display=swap">
<style>
:root{
  --orange:#e98f3f;
  --ink:#1d1d1f;
  --muted:#666;
  --soft:#e7ecf4;
  --card-line:#d9dde4;
  --dark:#2b2b2b;
  --white:#fff;
  --ph-warm:#f3e3d3;
  --ph-cool:#dde4ef;
}
*{box-sizing:border-box;margin:0;padding:0}
html,body{width:1200px;height:3263px;overflow:hidden}
body{font-family:"Poppins",sans-serif;color:var(--ink);background:var(--white);position:relative}
.abs{position:absolute}
section,header,nav,footer,.topbar{position:absolute;left:0;width:1200px}
.topbar{top:0;height:28px;background:var(--dark);color:#fff;font-size:9.5px}
.topbar span{position:absolute;top:8px}
.header{top:28px;height:68px;background:#eef1f6}
.logo{display:flex;align-items:center;gap:8px}
.logo-mark{width:12px;height:12px;background:var(--orange);flex:none}
.logo-name{font-size:22px;font-weight:600;color:var(--orange);line-height:1}
.logo-sub{font-size:8.5px;font-weight:600;color:#333;margin-top:3px;text-align:right}
.search{left:352px;top:18px;width:437px;height:32px;background:#fff;border-radius:3px;font-size:9px;color:#333}
.search .cat{position:absolute;left:12px;top:10px}
.search .div{position:absolute;left:92px;top:8px;width:1px;height:16px;background:#e3e3e3}
.search .q{position:absolute;left:103px;top:10px;color:#888}
.search .btn{position:absolute;right:0;top:0;width:37px;height:32px;background:var(--orange);border-radius:0 3px 3px 0}
.header-links{right:160px;top:27px;display:flex;gap:16px;font-size:10.5px;color:#444;align-items:center}
.header-links span{display:flex;align-items:center;gap:5px}
.nav{top:96px;height:38px;background:var(--orange);display:flex;justify-content:center;gap:22px;color:#fff;font-size:10.5px;align-items:center}
.hero{top:134px;height:415px;background:#fff}
.hero-kicker{left:151px;top:88px;font-size:12px;color:var(--orange);font-weight:500}
.hero h1{position:absolute;left:151px;top:110px;font-size:39px;font-weight:500;line-height:1.13;width:520px}
.hero-price{left:151px;top:212px;color:var(--orange);font-size:11px}
.hero-price b{font-size:32px;font-weight:500;margin-left:4px}
.hero-price sup{font-size:16px}
.btn-orange{background:var(--orange);color:#fff;font-size:10px;display:flex;align-items:center;justify-content:center}
.hero-img{left:625px;top:84px;width:442px;height:300px;border-radius:6px;background:linear-gradient(160deg,#e4efe6 0%,#e6ebf5 55%,#f3ead8 100%)}
.arrow{width:20px;height:20px}
.features{left:160px;top:512px;width:880px;height:83px;background:var(--orange);border-radius:3px;display:flex;color:#fff}
.features div{flex:1;text-align:center;border-right:1px solid rgba(255,255,255,.35);margin:12px 0;padding-top:10px}
.features div:last-child{border:none}
.features h4{font-size:12.5px;font-weight:500}
.features p{font-size:10px;margin-top:5px}
.band-soft{background:var(--soft)}
.promos{top:549px;height:375px}
.promo{top:130px;height:169px;border-radius:3px;color:#fff;overflow:hidden}
.promo .txt{position:absolute;top:28px}
.promo small{font-size:9.5px;display:block}
.promo h3{font-size:17px;font-weight:500;line-height:1.1;margin-top:8px}
.promo .from{font-size:11px;margin-top:6px}
.promo .shop{margin-top:12px;background:#1d1d1f;color:#fff;font-size:8.5px;padding:6px 8px;display:inline-block}
.promo .pic{position:absolute;top:0;height:169px}
.section-white{background:#fff}
.eyebrow{width:100%;text-align:center;font-size:12.5px}
.title{width:100%;text-align:center;font-size:24px;font-weight:500}
.card{width:140px;height:233px;background:#fff;border:1px solid var(--card-line);border-radius:3px}
.card .pic{position:absolute;left:10px;top:10px;width:118px;height:116px;border-radius:3px}
.badge{position:absolute;right:8px;top:7px;background:#e34b2d;color:#fff;font-size:7.5px;padding:1px 5px;border-radius:8px}
.card .stars{position:absolute;left:9px;top:130px;font-size:7.5px;color:var(--orange)}
.card .stars i{color:#999;font-style:normal}
.card .name{position:absolute;left:9px;top:141px;font-size:9px;line-height:1.25;width:120px}
.card .price{position:absolute;left:9px;top:167px;font-size:10.5px;font-weight:500}
.card .price s{font-size:7.5px;color:#aaa;margin-left:4px;font-weight:400}
.card .add{position:absolute;left:30px;top:198px;width:82px;height:22px;background:#1d1d1f;color:#fff;font-size:8px;display:flex;align-items:center;justify-content:center}
.sq-arrow{width:21px;height:21px;background:var(--orange);color:#fff;font-size:12px;display:flex;align-items:center;justify-content:center;border-radius:2px}
.sale{top:1375px;height:495px}
.sale .best{width:100%;text-align:center;top:103px;font-size:33px;color:var(--orange);font-weight:500;letter-spacing:1px}
.sale .offer{width:100%;text-align:center;top:146px;font-size:32px;line-height:1.2;font-weight:500}
.offer-box{left:461px;top:267px;width:278px;height:156px;background:#161616;color:#fff}
.person{top:60px;height:435px;border-radius:4px 4px 0 0}
.reviews{top:2319px;height:458px}
.review{top:141px;width:280px;height:229px;background:#f8f9fb;border-bottom:2px solid var(--orange)}
.review .av{position:absolute;left:22px;top:24px;width:42px;height:42px;border-radius:50%;background:#f0c14a}
.review .who{position:absolute;left:78px;top:32px;font-size:12px}
.review .who small{display:block;font-size:8px;color:#999;margin-top:3px}
.review .q{position:absolute;right:20px;top:26px;width:40px;height:28px}
.review h4{position:absolute;left:22px;top:90px;color:var(--orange);font-size:14px;font-weight:500}
.review p{position:absolute;left:22px;top:122px;width:240px;font-size:9px;line-height:1.6;color:#555}
.review .rs{position:absolute;left:22px;top:193px;color:var(--orange);font-size:13px;letter-spacing:1px}
.subscribe{top:2777px;height:219px}
.footer{top:2996px;height:228px}
.footer h5{font-size:12px;font-weight:500}
.footer ul{list-style:none;margin-top:10px;font-size:10px;color:var(--muted);line-height:18.6px}
.social{display:flex;gap:7px}
.social span{width:21px;height:21px;background:var(--orange)}
.cards-pay{display:flex;gap:5px}
.cards-pay span{width:37px;height:23px;background:#fff;border:1px solid #ddd;border-radius:2px}
.copyright{top:3224px;height:39px;background:var(--dark);color:#fff;font-size:9.5px;text-align:center;line-height:39px}
</style>
</head>
<body>

<div class="topbar">
  <span style="left:160px">Need virtual style advice? / +1 555 014 7720</span>
  <span style="left:809px">Track my Order</span>
  <span style="left:915px">Dollar (USD) ▾</span>
  <span style="left:1013px">ENG ▾</span>
</div>

<header class="header">
  <div class="abs logo" style="left:160px;top:18px">
    <div class="logo-mark"></div>
    <div><div class="logo-name">Bluefern</div><div class="logo-sub">Safety Products</div></div>
  </div>
  <div class="abs search">
    <span class="cat">All Categories ▾</span><span class="div"></span>
    <span class="q">what do you need?</span>
    <span class="btn"><svg width="37" height="32" viewBox="0 0 37 32"><circle cx="17" cy="15" r="5" fill="none" stroke="#fff" stroke-width="1.5"/><line x1="21" y1="19" x2="24" y2="22" stroke="#fff" stroke-width="1.5"/></svg></span>
  </div>
  <div class="abs header-links">
    <span><svg width="12" height="11" viewBox="0 0 12 11"><path d="M6 10 1.5 5.5A2.6 2.6 0 0 1 6 2a2.6 2.6 0 0 1 4.5 3.5z" fill="none" stroke="#444"/></svg>Wishlist</span>
    <span><svg width="13" height="12" viewBox="0 0 13 12"><path d="M1 1h2l1.5 7h6.5l1-5H4" fill="none" stroke="#444"/><circle cx="5" cy="10.5" r="1" fill="#444"/><circle cx="10" cy="10.5" r="1" fill="#444"/></svg>My cart</span>
    <span><svg width="11" height="12" viewBox="0 0 11 12"><circle cx="5.5" cy="3.5" r="2.5" fill="none" stroke="#444"/><path d="M1 11a4.5 4.5 0 0 1 9 0" fill="none" stroke="#444"/></svg>Sign in</span>
  </div>
</header>

<nav class="nav"><span>Home</span><span>Store ▾</span><span>Shop ▾</span><span>Engine Parts ▾</span><span>Head lights ▾</span><span>Contact</span></nav>

<section class="hero">
  <div class="abs hero-kicker">One day only flash sale</div>
  <h1>Best Trending Collection 2023 for you</h1>
  <div class="abs hero-price">Start at: <b>$79.<sup>99</sup></b></div>
  <div class="abs btn-orange" style="left:151px;top:279px;width:102px;height:33px">Buy Now →</div>
  <div class="abs hero-img" role="img" aria-label="Safety gear set: green hard hat, goggles, work gloves, respirator mask and coveralls"></div>
  <svg class="abs arrow" style="left:60px;top:182px" viewBox="0 0 20 20"><path d="M13 2 5 10l8 8" fill="none" stroke="#333" stroke-width="1.6"/></svg>
  <svg class="abs arrow" style="left:1110px;top:182px" viewBox="0 0 20 20"><path d="M7 2l8 8-8 8" fill="none" stroke="#333" stroke-width="1.6"/></svg>
</section>

<section class="promos band-soft">
  <div class="abs promo" style="left:160px;width:281px;background:#3f57b8">
    <div class="pic" role="img" aria-label="Gloves, face mask and respirator on blue background" style="left:165px;width:116px;background:linear-gradient(180deg,#4d66c2,#6f86cf)"></div>
    <div class="txt" style="left:20px"><small>Best Collection 2023</small><h3>Workplace Safety<br>Gear</h3><div class="from" style="color:#f5a35a">Start From $123.⁴⁹</div><span class="shop">Shop Now →</span></div>
  </div>
  <div class="abs promo" style="left:460px;width:281px;background:#d9663f">
    <div class="pic" role="img" aria-label="Orange and black multi-purpose work gloves" style="left:0;width:112px;background:linear-gradient(180deg,#d56a45,#c75c38)"></div>
    <div class="txt" style="left:123px"><small>Best Collection 2023</small><h3>Safety Multi<br>purpose Gloves</h3><div class="from">Start From $49.²³</div><span class="shop">Shop Now →</span></div>
  </div>
  <div class="abs promo" style="left:755px;width:280px;background:#79b9e9">
    <div class="pic" role="img" aria-label="Worker in hard hat, safety glasses and hi-vis vest" style="left:0;width:135px;background:linear-gradient(180deg,#8cc3ec,#a9cfe0)"></div>
    <div class="txt" style="left:142px"><small>Best Collection 2023</small><h3>Safety Glasses</h3><div class="from">52.²³ <s style="font-size:8px">$125.⁴⁴</s></div><span class="shop">Shop Now →</span></div>
  </div>
  <div class="abs features" style="top:-37px">
    <div><h4>Taped High Vis</h4><p>Best Tool for safety</p></div>
    <div><h4>Drillers &amp; Cutter</h4><p>Get 20% flat Offers</p></div>
    <div><h4>Industrial Goggles</h4><p>Buy a good quality Products</p></div>
    <div><h4>Safety Boots</h4><p>35% Flat Offers</p></div>
    <div><h4>Full body protective Suits</h4><p>Special Offers for best Suit</p></div>
  </div>
</section>

<section class="section-white" style="top:924px;height:451px">
  <div class="abs eyebrow" style="top:58px">Best Safety Products</div>
  <div class="abs title" style="top:76px">Work Clothing, Safety Boots &amp; Shoes, PPE Safety</div>
  <div class="abs sq-arrow" style="left:134px;top:241px">‹</div>
  <div class="abs sq-arrow" style="left:1039px;top:243px">›</div>
  <div class="abs card" style="left:160px;top:134px"><div class="pic" role="img" aria-label="Clear safety goggles" style="background:#f1f2f4"></div><span class="badge">-10%</span><div class="stars">★★★★<i>☆ (18)</i></div><div class="name">Industrial Goggles Anti Fog...</div><div class="price">$399.00<s>$699.50</s></div><div class="add">Add to Cart</div></div>
  <div class="abs card" style="left:307px;top:134px"><div class="pic" role="img" aria-label="Orange hi-vis work shirt" style="background:var(--ph-warm)"></div><span class="badge">-10%</span><div class="stars">★★★★<i>☆ (18)</i></div><div class="name">Industrial Goggles Anti Fog...</div><div class="price">$399.00<s>$699.50</s></div><div class="add">Add to Cart</div></div>
  <div class="abs card" style="left:454px;top:134px"><div class="pic" role="img" aria-label="Ear defender headset" style="background:#ebe6e7"></div><span class="badge">-10%</span><div class="stars">★★★★<i>☆ (18)</i></div><div class="name">Industrial Goggles Anti Fog...</div><div class="price">$399.00<s>$699.50</s></div><div class="add">Add to Cart</div></div>
  <div class="abs card" style="left:601px;top:134px"><div class="pic" role="img" aria-label="Blue hard hat" style="background:var(--ph-cool)"></div><span class="badge">-10%</span><div class="stars">★★★★<i>☆ (18)</i></div><div class="name">Industrial Goggles Anti Fog...</div><div class="price">$399.00<s>$699.50</s></div><div class="add">Add to Cart</div></div>
  <div class="abs card" style="left:748px;top:134px"><div class="pic" role="img" aria-label="White protective coverall suit" style="background:#f3f5f9"></div><span class="badge">-10%</span><div class="stars">★★★★<i>☆ (18)</i></div><div class="name">Industrial Goggles Anti Fog...</div><div class="price">$399.00<s>$699.50</s></div><div class="add">Add to Cart</div></div>
  <div class="abs card" style="left:895px;top:134px"><div class="pic" role="img" aria-label="Navy safety boot" style="background:var(--ph-cool)"></div><span class="badge">-10%</span><div class="stars">★★★★<i>☆ (18)</i></div><div class="name">Industrial Goggles Anti Fog...</div><div class="price">$399.00<s>$699.50</s></div><div class="add">Add to Cart</div></div>
</section>

<section class="sale band-soft">
  <div class="abs person" role="img" aria-label="Worker in orange hard hat, goggles and respirator giving a thumbs up" style="left:101px;width:292px;background:linear-gradient(180deg,#dfe4ec,#d3d9e3)"></div>
  <div class="abs person" role="img" aria-label="Worker in orange hard hat and yellow hi-vis vest" style="left:811px;width:352px;background:linear-gradient(180deg,#dfe4ec,#d3d9e3)"></div>
  <div class="abs eyebrow" style="top:78px">Latest Collection of 2023</div>
  <div class="abs best">BEST SALE</div>
  <div class="abs offer">Special Offer<br>safety wear clothing</div>
  <div class="abs offer-box">
    <div class="abs" style="left:0;width:278px;text-align:center;top:22px;font-size:33px;color:var(--orange);font-weight:300;letter-spacing:2px">UPTO</div>
    <div class="abs" style="left:45px;top:64px;font-size:58px;font-weight:500">50%</div>
    <div class="abs" style="left:185px;top:110px;font-size:20px;font-weight:300">OFF</div>
  </div>
</section>

<section class="section-white" style="top:1870px;height:449px">
  <div class="abs eyebrow" style="top:57px">New Products</div>
  <div class="abs title" style="top:76px">Work Clothing, Safety Boots &amp; Shoes, PPE Safety</div>
  <div class="abs sq-arrow" style="left:134px;top:239px">‹</div>
  <div class="abs sq-arrow" style="left:1039px;top:241px">›</div>
  <div class="abs card" style="left:160px;top:134px"><div class="pic" role="img" aria-label="Clear safety goggles" style="background:#f1f2f4"></div><span class="badge">-10%</span><div class="stars">★★★★<i>☆ (18)</i></div><div class="name">Industrial Goggles Anti Fog...</div><div class="price">$399.00<s>$699.50</s></div><div class="add">Add to Cart</div></div>
  <div class="abs card" style="left:307px;top:134px"><div class="pic" role="img" aria-label="Orange hi-vis work shirt" style="background:var(--ph-warm)"></div><span class="badge">-10%</span><div class="stars">★★★★<i>☆ (18)</i></div><div class="name">Industrial Goggles Anti Fog...</div><div class="price">$399.00<s>$699.50</s></div><div class="add">Add to Cart</div></div>
  <div class="abs card" style="left:454px;top:134px"><div class="pic" role="img" aria-label="Ear defender headset" style="background:#ebe6e7"></div><span class="badge">-10%</span><div class="stars">★★★★<i>☆ (18)</i></div><div class="name">Industrial Goggles Anti Fog...</div><div class="price">$399.00<s>$699.50</s></div><div class="add">Add to Cart</div></div>
  <div class="abs card" style="left:601px;top:134px"><div class="pic" role="img" aria-label="Blue hard hat" style="background:var(--ph-cool)"></div><span class="badge">-10%</span><div class="stars">★★★★<i>☆ (18)</i></div><div class="name">Industrial Goggles Anti Fog...</div><div class="price">$399.00<s>$699.50</s></div><div class="add">Add to Cart</div></div>
  <div class="abs card" style="left:748px;top:134px"><div class="pic" role="img" aria-label="White protective coverall suit" style="background:#f3f5f9"></div><span class="badge">-10%</span><div class="stars">★★★★<i>☆ (18)</i></div><div class="name">Industrial Goggles Anti Fog...</div><div class="price">$399.00<s>$699.50</s></div><div class="add">Add to Cart</div></div>
  <div class="abs card" style="left:895px;top:134px"><div class="pic" role="img" aria-label="Navy safety boot" style="background:var(--ph-cool)"></div><span class="badge">-10%</span><div class="stars">★★★★<i>☆ (18)</i></div><div class="name">Industrial Goggles Anti Fog...</div><div class="price">$399.00<s>$699.50</s></div><div class="add">Add to Cart</div></div>
</section>

<section class="reviews band-soft">
  <div class="abs eyebrow" style="top:52px">Client Reviews</div>
  <div class="abs title" style="top:73px">We Love Our Clients! Trust Our Customer</div>
  <div class="abs review" style="left:160px"><div class="av" role="img" aria-label="Reviewer avatar"></div><div class="who">John Doe<small>Designer</small></div><svg class="q" viewBox="0 0 40 28"><path d="M2 2h14v14l-7 10V16H2z M22 2h14v14l-7 10V16h-7z" fill="none" stroke="#c9c9c9" stroke-width="1.5"/></svg><h4>Great Course !</h4><p>Lorem Ipsum is simply dummy text of the printing and typesetting industry. Lorem Ipsum has been the industry's standard dummy text ever since the 1500s, when an unknown printer took a galley of type and</p><div class="rs">★★★★☆</div></div>
  <div class="abs review" style="left:457px"><div class="av" role="img" aria-label="Reviewer avatar"></div><div class="who">John Doe<small>Designer</small></div><svg class="q" viewBox="0 0 40 28"><path d="M2 2h14v14l-7 10V16H2z M22 2h14v14l-7 10V16h-7z" fill="none" stroke="#c9c9c9" stroke-width="1.5"/></svg><h4>Great Course !</h4><p>Lorem Ipsum is simply dummy text of the printing and typesetting industry. Lorem Ipsum has been the industry's standard dummy text ever since the 1500s, when an unknown printer took a galley of type and</p><div class="rs">★★★★☆</div></div>
  <div class="abs review" style="left:755px"><div class="av" role="img" aria-label="Reviewer avatar"></div><div class="who">John Doe<small>Designer</small></div><svg class="q" viewBox="0 0 40 28"><path d="M2 2h14v14l-7 10V16H2z M22 2h14v14l-7 10V16h-7z" fill="none" stroke="#c9c9c9" stroke-width="1.5"/></svg><h4>Great Course !</h4><p>Lorem Ipsum is simply dummy text of the printing and typesetting industry. Lorem Ipsum has been the industry's standard dummy text ever since the 1500s, when an unknown printer took a galley of type and</p><div class="rs">★★★★☆</div></div>
</section>

<section class="subscribe section-white">
  <div class="abs eyebrow" style="top:55px">Subscribe Now</div>
  <div class="abs title" style="top:75px">Be the first to know about new arrivals, look</div>
  <div class="abs" style="left:381px;top:129px;width:328px;height:31px;background:var(--soft);font-size:9.5px;padding:9px 15px">Enter Email</div>
  <div class="abs btn-orange" style="left:709px;top:129px;width:109px;height:31px;font-size:10.5px">Subscribe Now</div>
</section>

<footer class="footer band-soft">
  <div class="abs logo" style="left:160px;top:38px">
    <div class="logo-mark"></div>
    <div><div class="logo-name">Bluefern</div><div class="logo-sub">Safety Products</div></div>
  </div>
  <p class="abs" style="left:160px;top:95px;width:260px;font-size:10px;line-height:15.5px;color:#333">Proin varius iaculis orci, nec pretium purus porttitor et. Morbi arcu elit, porta et imperdiet ut, gravida et justo. Mauris sed mollis libero.</p>
  <div class="abs social" style="left:160px;top:177px"><span></span><span></span><span></span><span></span></div>
  <div class="abs" style="left:460px;top:44px"><h5>Quick Links</h5><ul><li>About</li><li>Terms &amp; Conditions</li><li>Privacy Policy</li><li>Shop</li><li>Contact</li></ul></div>
  <div class="abs" style="left:609px;top:44px"><h5>Support</h5><ul><li>Help</li><li>Contact Us</li><li>Feedback</li><li>Unsubscribe</li><li>Reservations</li></ul></div>
  <div class="abs" style="left:760px;top:44px;width:280px"><h5>Contact Us</h5><p style="font-size:10px;color:var(--muted);line-height:18.6px;margin-top:10px">Address: lorem ipsum USA Lorem ipsum is dolor amet lorem ipsum<br>E-mail: info@example.com</p></div>
  <div class="abs cards-pay" style="left:760px;top:149px"><span></span><span></span><span></span><span></span></div>
</footer>

<div class="copyright abs" style="left:0;width:1200px">Copyright 2023 bluefernworks.com All Rights Reserved.</div>

</body>
</html>
```